Flyer Design Project - Bra Shop

Hi all,

I want to have a flyer with theme colour Pink or Red.
I will upload one of my previous flyers.

requirement:
*I need to keep the contact detail, address and map.(you can edit it as different style if you want.)

*I need to keep our store logo and store name:
Velmotine
Lingerie

*The information in flyer:

We sell
Push / non push up bras
Maternity
Silqe
Bottoms
Pajamas
Shape wears
Sexy lingerie
Stockings, suspenders
Garters
Crystal phonecase
And much more

*At the top right coner of flyer, please write down '$10 Voucher' because I want it to be a Voucher.

*At the bottom of the flyer, please write (small font size ):
"**Only one flyer voucher can be used in one purchase when price is above $50 and below $100. Two flyer vouchers can be used in one purchase when price is not less than $100.

aged 30+ to 70; they are relatively wealthy.

Store

• the footnote changed:

**Only one flyer voucher can be used in one purchase when price is above $50 and below $100. Two flyer vouchers can be used in one purchase when price is not less than $100.
• I don't want a lady or people on flyer.
thanks

```html
<!DOCTYPE html>
<html lang="en">
<head>
<meta charset="utf-8">
<title>Velmotine Lingerie – Flyer</title>
<link rel="stylesheet" href="https://fonts.googleapis.com/css2?family=Arimo:wght@400;700&display=swap">
<style>
  :root {
    --magenta-core: #e41fd4;
    --magenta-mid: #c512b4;
    --magenta-edge: #92067f;
    --white: #ffffff;
    --bubble: rgba(255, 255, 255, 0.07);
    --voucher-ring: #f03ee6;
    --voucher-fill: #d414c4;
    --garment-light: #f25bd8;
    --garment-deep: #c9179f;
    --map-tone: rgba(255, 255, 255, 0.16);
  }
  * { margin: 0; padding: 0; box-sizing: border-box; }
  html, body { width: 1200px; height: 848px; overflow: hidden; background: var(--magenta-edge); }
  .flyer {
    position: relative;
    width: 1200px;
    height: 848px;
    overflow: hidden;
    font-family: "Arimo", Arial, sans-serif;
    color: var(--white);
    background: radial-gradient(ellipse 70% 75% at 42% 52%, var(--magenta-core) 0%, var(--magenta-mid) 45%, var(--magenta-edge) 100%);
  }
  .bubbles { position: absolute; inset: 0; width: 1200px; height: 848px; }
  .bubbles circle { fill: var(--bubble); }

  .garment-visual {
    position: absolute;
    left: 0; top: 0;
    width: 150px; height: 520px;
    background: linear-gradient(160deg, var(--garment-light) 0%, var(--garment-deep) 100%);
    border-radius: 0 0 70px 30px;
    opacity: 0.85;
  }

  .brand {
    position: absolute;
    left: 0; width: 1200px;
    top: 100px;
    text-align: center;
  }
  .brand-name {
    display: block;
    font-size: 66px;
    font-weight: 700;
    letter-spacing: 1px;
    line-height: 1;
  }
  .brand-tagline {
    display: block;
    margin-top: 14px;
    font-size: 25px;
    font-weight: 400;
    letter-spacing: 16px;
    padding-left: 16px;
  }

  .voucher {
    position: absolute;
    left: 952px; top: 50px;
    width: 172px; height: 172px;
    border-radius: 50%;
    background: var(--voucher-fill);
    border: 8px solid var(--voucher-ring);
    box-shadow: 0 10px 24px rgba(90, 0, 80, 0.35);
    text-align: center;
    padding-top: 26px;
  }
  .voucher-amount { display: block; font-size: 60px; font-weight: 700; line-height: 1; }
  .voucher-label { display: block; font-size: 23px; font-weight: 700; margin-top: 4px; }

  .product-list {
    position: absolute;
    left: 166px; top: 262px;
    list-style: none;
    display: grid;
    grid-auto-flow: column;
    grid-template-rows: repeat(6, auto);
    grid-template-columns: 514px auto;
    font-size: 38px;
    font-weight: 700;
    line-height: 1.12;
  }

  .store-info {
    position: absolute;
    left: 54px; top: 540px;
    font-size: 22px;
    font-weight: 700;
    line-height: 1.42;
  }
  .store-address { margin-top: 22px; font-style: normal; }

  .footnote {
    position: absolute;
    left: 52px; top: 772px;
    width: 700px;
    font-size: 13.5px;
    font-weight: 400;
    line-height: 1.45;
  }

  .location-map {
    position: absolute;
    left: 826px; top: 520px;
    width: 374px; height: 328px;
    background: linear-gradient(150deg, var(--map-tone), rgba(255,255,255,0.04));
    border-top-left-radius: 40px;
  }
</style>
</head>
<body>
<main class="flyer">
  <svg class="bubbles" viewBox="0 0 1200 848" aria-hidden="true">
    <circle cx="315" cy="100" r="70"/>
    <circle cx="760" cy="262" r="150"/>
    <circle cx="1070" cy="170" r="95"/>
    <circle cx="1120" cy="660" r="210"/>
    <circle cx="60" cy="520" r="80"/>
  </svg>

  <div class="garment-visual" role="img" aria-label="Pink bra hanging from its strap"></div>

  <header class="brand">
    <span class="brand-name">Velmotine</span>
    <span class="brand-tagline">Lingerie</span>
  </header>

  <div class="voucher">
    <span class="voucher-amount">$10</span>
    <span class="voucher-label">* Voucher</span>
  </div>

  <ul class="product-list">
    <li>Push / non push up bras</li>
    <li>Maternity</li>
    <li>Silqe</li>
    <li>Bottoms</li>
    <li>Pajamas</li>
    <li>Shape wears</li>
    <li>Sexy lingerie</li>
    <li>Stockings, suspenders</li>
    <li>Garters</li>
    <li>Crystal phonecase</li>
    <li>And much more</li>
  </ul>

  <section class="store-info">
    <p class="store-hours">Open hour:<br>Mon - Sat 10:00 am - 5:30 pm<br>Sun 10:00 am - 5:30 pm</p>
    <address class="store-address">Address: Shop 5/218<br>Harbour Vale Rd, NSW 2031<br>Phone: 02 9000 4417</address>
  </section>

  <div class="location-map" role="img" aria-label="Street map showing the shop on Harbour Vale Rd near two side streets"></div>

  <p class="footnote">* Only one flyer voucher can be used in one purchase when price is above $50 and below $100.<br>Two flyer vouchers can be used in one purchase when price &nbsp;is not less than $100.</p>
</main>
</body>
</html>
```